Varen Psychiatry (Psychiatry clinic offering cutting edge treatments)

2 sided flyer for new psychiatry practice in Boulder, CO. I want something that looks professional, cutting edge, but also welcoming and friendly. My logo and pictures are attached.

Some of the copy:
Personalized, holistic Psychiatry combined with cutting-edge, evidence-based treatments. Our personalized psychiatry plan includes a bio-psycho-social evaluation, personalized treatment plan, medical evaluation for underlying hormonal and electrolyte abnormalities, and genetic testing (when warranted).

We specialize in treatment-resistant depression and substance abuse. We also treat PTSD, Bipolar Disorder, OCD, anxiety disorders, ADHD, and psychotic disorders.

About Dr. Pim- Dr. Pim served as Chief Resident at the largest private psychiatry hospital in Colorado. While there he won 3 consecutive awards for exceptionally high Psychiatry in service test score (99th percentile). He was a board member of Westfield Psychiatric Guild and helped advocate for better Colorado mental health policy. Dr. Pim is uniquely trained in Ketamine, Transcranial Magnetic Stimulation, and integrative psychiatry.

Target Market(s)

Private pay mental health patients, planning to give out to psychologists and family practice doctors

Industry/Entity Type

Medicine/Psychiatry

Colors
0054AA
0677BA
7BADD7
CADEEF
E8F1F8
0094D4
00A9DD
6FCCEA
C7EBF8
E9F6FB
00AB8E
00BBA5
67D7C9
C6EFE9
E9F9F6

Requirements
Must have
• My logo, an about me (Dr. Tom Pim) section

```html
<!DOCTYPE html>
<html lang="en">
<head>
<meta charset="utf-8">
<title>Varen Psychiatry – Two-Sided Flyer</title>
<link href="https://fonts.googleapis.com/css2?family=Open+Sans:wght@400;600;700&family=Oswald:wght@400;500&display=swap" rel="stylesheet">
<style>
  :root{
    --stage:#8a8b8e;
    --paper:#ffffff;
    --navy:#27306b;
    --ink:#2b3a7c;
    --footer:#23264f;
    --teal:#5cc6da;
    --blue:#3d82c8;
    --purple:#8c52ad;
    --sky:#4fa3d6;
    --lav:#e8e7f3;
    --accent:#3b9cc4;
  }
  *{box-sizing:border-box;margin:0;padding:0}
  html,body{width:1200px;height:794px;overflow:hidden}
  body{background:var(--stage);font-family:"Open Sans",Arial,sans-serif;position:relative}
  .page{position:absolute;top:61px;width:514px;height:666px;background:var(--paper);box-shadow:4px 5px 8px rgba(0,0,0,.35);overflow:hidden}
  .page--front{left:55px}
  .page--back{left:624px}

  .brand{position:absolute;left:22px;top:22px;display:flex;align-items:center;gap:9px}
  .brand__dot{width:34px;height:34px;border-radius:50%;background:linear-gradient(135deg,var(--blue),var(--purple))}
  .brand__name{font-family:"Open Sans",sans-serif;font-weight:600;font-size:17px;letter-spacing:2px;color:#5f6470;line-height:1.05}
  .announce{position:absolute;right:25px;top:27px;text-align:right;font-family:"Oswald",sans-serif;font-weight:500;font-size:13.5px;line-height:15px;color:var(--navy);letter-spacing:-.1px}
  .announce span{color:var(--sky)}

  .hero{position:absolute;left:14px;top:69px;width:485px;height:237px;border-top-right-radius:34px}
  .hero--mind{background:linear-gradient(100deg,#dfe3ee 0%,#c9cfe3 38%,#8d7fb8 62%,#5a4d98 80%,#6a88c6 100%)}
  .hero--tech{top:69px;left:15px;width:484px;background:linear-gradient(110deg,#2c5f8d 0%,#5a9cc9 40%,#9ec7e4 60%,#3e7db2 85%,#274f7a 100%)}
  .hero__title{position:absolute;left:15px;top:80px;font-weight:700;font-size:13.2px;line-height:17.8px;color:var(--ink)}

  .intro{position:absolute;left:14px;top:313px;width:485px;font-size:9.3px;line-height:13px;color:var(--ink);text-align:justify}

  .conditions{position:absolute;left:0;top:363px;width:514px;height:65px;display:flex;background:linear-gradient(90deg,var(--teal),var(--blue) 55%,var(--purple))}
  .condition{flex:1;border-right:1px solid rgba(255,255,255,.35);display:flex;flex-direction:column;align-items:center;justify-content:flex-end;padding-bottom:5px;color:#fff;font-size:9.6px;line-height:11px;text-align:center}
  .condition:last-child{border-right:none}
  .condition svg{margin-bottom:auto;margin-top:7px}

  .body-copy{position:absolute;left:0;top:428px;width:514px;height:195px;background:var(--lav);padding:12px 14px 0}
  .body-copy p{font-size:7.5px;line-height:10.9px;color:var(--ink);text-align:justify;margin-bottom:11px}

  .contact{position:absolute;left:0;bottom:0;width:514px;height:43px;background:var(--footer);border-radius:18px 18px 0 0;display:flex;align-items:center;justify-content:space-between;padding:0 22px 0 16px;color:#fff;font-size:10.6px}
  .contact__item{display:flex;align-items:center;gap:5px}

  .feature{position:absolute;left:0;top:326px;width:514px;height:134px;background:linear-gradient(90deg,var(--teal),var(--blue) 50%,var(--purple));color:#fff;padding:0 16px 0 19px}
  .feature__title{text-align:center;font-weight:700;font-size:12.4px;line-height:18px;margin-top:12px;margin-bottom:9px}
  .feature p{font-size:8.4px;line-height:12px;letter-spacing:-.15px}

  .about{position:absolute;left:0;top:460px;width:514px;height:163px;background:var(--lav)}
  .about__name{position:absolute;left:17px;top:21px;font-weight:700;font-size:12.6px;color:var(--navy)}
  .about__bio{position:absolute;left:17px;top:43px;width:362px;font-size:7.3px;line-height:10.9px;color:var(--ink);text-align:justify}
  .about__photo{position:absolute;left:394px;top:36px;width:105px;height:102px;background:linear-gradient(135deg,#8c8c8c,#3f3f3f)}
  .about__cta{position:absolute;left:15px;top:140px;font-size:10.8px;color:var(--accent)}
</style>
</head>
<body>

<section class="page page--front">
  <div class="brand"><span class="brand__dot"></span><span class="brand__name">VAREN<br>PSYCHIATRY</span></div>
  <p class="announce">VAREN PSYCHIATRY IS NOW ACCEPTING<br>NEW PATIENTS IN <span>BOULDER, COLORADO!</span></p>

  <div class="hero hero--mind" role="img" aria-label="Photo of a woman's profile with a glowing digital brain network">
    <h1 class="hero__title">SPECIALIZING IN<br>EVIDENCE-BASED,<br>STATE-OF-THE-ART<br>MENTAL HEALTH<br>TREATMENT.</h1>
  </div>

  <p class="intro">We specialize in treating patients with treatment resistant depression and substance abuse disorders who have not responded to other forms of treatment. We believe that by providing comprehensive care, we can help our patients heal both emotionally and physically. We also treat patients with:</p>

  <ul class="conditions">
    <li class="condition"><svg width="28" height="28" viewBox="0 0 28 28"><circle cx="14" cy="14" r="12" fill="none" stroke="#fff" stroke-width="1.2"/></svg>PTSD</li>
    <li class="condition"><svg width="28" height="28" viewBox="0 0 28 28"><circle cx="14" cy="14" r="12" fill="none" stroke="#fff" stroke-width="1.2"/></svg>Bipolar<br>Disorder</li>
    <li class="condition"><svg width="28" height="28" viewBox="0 0 28 28"><circle cx="12" cy="12" r="9" fill="none" stroke="#fff" stroke-width="1.2"/><path d="M18.5 18.5 25 25" stroke="#fff" stroke-width="2"/></svg>OCD</li>
    <li class="condition"><svg width="28" height="28" viewBox="0 0 28 28"><circle cx="14" cy="14" r="12" fill="none" stroke="#fff" stroke-width="1.2"/></svg>Anxiety<br>Disorders</li>
    <li class="condition"><svg width="28" height="28" viewBox="0 0 28 28"><circle cx="14" cy="14" r="12" fill="none" stroke="#fff" stroke-width="1.2"/></svg>ADHD</li>
    <li class="condition"><svg width="28" height="28" viewBox="0 0 28 28"><circle cx="14" cy="14" r="12" fill="none" stroke="#fff" stroke-width="1.2"/></svg>Psychotic<br>Disorders</li>
  </ul>

  <div class="body-copy">
    <p>We know that mental health is complex and that multiple factors can contribute to the development of mental illness. For this reason, we take an integrative approach that considers the whole person. We understand that each individual has their own unique set of experiences, strengths, and challenges, and we tailor our treatment plans to suit each patient's personal needs.</p>
    <p>We know that mental health is complex and that multiple factors can contribute to the development of mental illness. For this reason, we take an integrative approach that considers the whole person. We understand that each individual has their own unique set of experiences, strengths, and challenges, and we tailor our treatment plans toaSo often, when we think about mental health, we focus on just treating symptoms. If someone is depressed, they might take medication to help them feel better. If someone is anxious, they might see a therapist to help them manage their anxiety.</p>
    <p>While these treatments can be helpful, they only address the symptoms of mental illness. To truly address mental health, it is necessary to treat the root causes. This might involve addressing childhood trauma, unresolved conflict, or feelings of worthlessness. It might also involve developing healthy coping mechanisms and learning how to set boundaries. By treating the root causes of mental illness, we can begin to create lasting change. suit each patient's personal needs.</p>
  </div>

  <footer class="contact">
    <span class="contact__item"><svg width="10" height="10" viewBox="0 0 10 10"><circle cx="5" cy="5" r="4.3" fill="none" stroke="#fff" stroke-width=".9"/><circle cx="5" cy="4.3" r="1.3" fill="#fff"/></svg>1180 Larkspur Ave. Boulder, CO 80302 #210</span>
    <span class="contact__item"><svg width="10" height="10" viewBox="0 0 10 10"><circle cx="5" cy="5" r="4.3" fill="none" stroke="#fff" stroke-width=".9"/><path d="M3.3 3l1 1-.5.7a3 3 0 0 0 1.5 1.5l.7-.5 1 1-.7.8C4.6 7.3 2.7 5.4 2.5 3.7z" fill="#fff"/></svg>303-555-0142</span>
    <span class="contact__item"><svg width="10" height="10" viewBox="0 0 10 10"><circle cx="5" cy="5" r="4.3" fill="none" stroke="#fff" stroke-width=".9"/><circle cx="5" cy="5" r="2.5" fill="none" stroke="#fff" stroke-width=".7"/></svg>www.varenpsych.com</span>
  </footer>
</section>

<section class="page page--back">
  <div class="brand"><span class="brand__dot"></span><span class="brand__name">VAREN<br>PSYCHIATRY</span></div>
  <p class="announce">VAREN PSYCHIATRY IS NOW ACCEPTING<br>NEW PATIENTS IN <span>BOULDER, COLORADO!</span></p>

  <div class="hero hero--tech" role="img" aria-label="Photo of a doctor with a stethoscope touching a digital screen showing a brain network"></div>

  <div class="feature">
    <h2 class="feature__title">SPECIALIZING IN EVIDENCE-BASED, STATE-OF-THE-ART<br>MENTAL HEALTH TREATMENT.</h2>
    <p>Our personalized psychiatry plan includes a bio-psycho-social evaluation, tailored treatment plan, medical evaluation for underlying hormonal and electrolyte abnormalities, and genetic testing (when warranted). Our integrative psychiatry approach combines cutting edge, evidence-based treatments with holistic therapies to provide you with the best possible care. In addition, we also offer Ketamine Assisted Therapy, TMS (Transcranial Magnetic Simulation), and MAT Treatment for Substance abuse. We pride ourselves on always staying up to date on the latest mental health treatments.</p>
  </div>

  <div class="about">
    <h3 class="about__name">DR. TOM PIM</h3>
    <p class="about__bio">Dr. Tom Pim is a psychiatrist with years of experience providing compassionate, evidence-based care to patients of all ages. He is uniquely trained in several cutting-edge treatments, including Ketamine, Transcranial Magnetic Stimulation (TMS), and integrative psychiatry. Prior to founding Varen Psychiatry, Dr. Pim served as Chief Resident at the largest private psychiatry hospital in Colorado. While there, he won three consecutive awards for exceptionally high Psychiatry in-service test scores (99th percentile). In addition, he was a board member of the Westfield Psychiatric Guild and helped advocate for better Colorado mental health policy. Thanks to his extensive training and experience, Dr. Pim is able to provide each patient with an individualized treatment plan that brings optimum results.</p>
    <div class="about__photo" role="img" aria-label="Portrait photo of Dr. Tom Pim"></div>
    <p class="about__cta">Get started with Varen, today!</p>
  </div>

  <footer class="contact">
    <span class="contact__item"><svg width="10" height="10" viewBox="0 0 10 10"><circle cx="5" cy="5" r="4.3" fill="none" stroke="#fff" stroke-width=".9"/><circle cx="5" cy="4.3" r="1.3" fill="#fff"/></svg>1180 Larkspur Ave. Boulder, CO 80302 #210</span>
    <span class="contact__item"><svg width="10" height="10" viewBox="0 0 10 10"><circle cx="5" cy="5" r="4.3" fill="none" stroke="#fff" stroke-width=".9"/><path d="M3.3 3l1 1-.5.7a3 3 0 0 0 1.5 1.5l.7-.5 1 1-.7.8C4.6 7.3 2.7 5.4 2.5 3.7z" fill="#fff"/></svg>303-555-0142</span>
    <span class="contact__item"><svg width="10" height="10" viewBox="0 0 10 10"><circle cx="5" cy="5" r="4.3" fill="none" stroke="#fff" stroke-width=".9"/><circle cx="5" cy="5" r="2.5" fill="none" stroke="#fff" stroke-width=".7"/></svg>www.varenpsych.com</span>
  </footer>
</section>

</body>
</html>
```